Meridian Capital Forward Summit Web Page Banner

I would like a banner with Conference Logo and Pictures from previous conferences, fading in and out whilst the logo remain stationery. Pictures of people, patients, doctors, community, hospital. Financial initiative conference of health service providers. Financing is essential to healthcare, hence ways of improving healthcare at the same time making it more affordable to the patients is the primary objective for the Conference.

Target Market(s)

Financial Health Services

Industry/Entity Type

Financial

Number of Pages Required

1 page

Colors
0492cd
ffc214
ec1f27
9bcb3b
e34197
0392cd

Requirements
Must have
• This banner should fit into one of Wordpress, themes. I will send the person the theme that is being used to ensure it fits with the site.

```html
<!DOCTYPE html>
<html lang="en">
<head>
<meta charset="utf-8">
<title>Meridian Capital Forward Summit – Web Banner</title>
<link rel="stylesheet" href="https://fonts.googleapis.com/css2?family=Arimo:wght@700&family=Roboto+Condensed:wght@700&family=PT+Sans:wght@400;700&display=swap">
<style>
  :root {
    --page-bg: #f0eed6;
    --band-green: #9bcb3b;
    --accent-yellow: #ffc214;
    --accent-blue: #0492cd;
    --accent-red: #ec1f27;
    --accent-pink: #e34197;
    --ink: #000000;
    --ink-soft: #3a3a3a;
    --panel: #ffffff;
    --hex-grey: #e4e4e4;
  }
  * { margin: 0; padding: 0; box-sizing: border-box; }
  html, body { width: 1200px; height: 900px; overflow: hidden; }
  body { background: var(--page-bg); position: relative; font-family: "Arimo", Arial, sans-serif; }

  .banner {
    position: absolute; left: 207px; top: 296px;
    width: 786px; height: 267px;
    background: var(--panel);
    overflow: hidden;
  }
  .banner__head {
    position: absolute; left: 0; top: 0; width: 100%; height: 117px;
    background: var(--band-green);
  }
  .banner__rule {
    position: absolute; left: 0; top: 117px; width: 100%; height: 6px;
    background: var(--accent-yellow);
    box-shadow: 0 3px 4px rgba(0,0,0,0.12);
  }

  .summit-mark {
    position: absolute; left: 18px; top: 22px;
    display: flex; align-items: center; gap: 8px;
    width: 170px;
  }
  .summit-mark__dot {
    flex: none; width: 36px; height: 36px; border-radius: 50%;
    background: var(--accent-yellow);
  }
  .summit-mark__name {
    font-family: "Roboto Condensed", "Arial Narrow", sans-serif; font-weight: 700;
    font-size: 14px; line-height: 16px; color: var(--ink-soft);
    text-transform: uppercase;
  }
  .summit-mark__place {
    position: absolute; left: 36px; top: 94px;
    font-family: "PT Sans", Arial, sans-serif; font-weight: 700;
    font-size: 8px; letter-spacing: 0.6px; color: var(--ink-soft);
    border-top: 1px solid var(--ink-soft); padding-top: 1px; width: 140px;
  }

  .headline {
    position: absolute; right: 24px; top: 26px; text-align: right; color: var(--ink);
    white-space: nowrap;
  }
  .headline__title {
    font-family: "Roboto Condensed", "Arial Narrow", sans-serif; font-weight: 700;
    font-size: 36px; line-height: 38px;
  }
  .headline__sub {
    font-family: "Arimo", Arial, sans-serif; font-weight: 700;
    font-size: 22px; line-height: 26px;
  }
  .headline__date {
    font-family: "Arimo", Arial, sans-serif; font-weight: 700;
    font-size: 13px; line-height: 16px; margin-top: 8px;
  }

  .hex-field {
    position: absolute; left: 0; top: 123px; width: 112px; height: 130px;
    background: linear-gradient(100deg, var(--hex-grey) 0%, rgba(228,228,228,0.4) 55%, rgba(255,255,255,0) 100%);
  }

  .gallery {
    position: absolute; left: 41px; top: 136px;
    display: flex; gap: 4px;
  }
  .gallery__photo {
    width: 84.5px; height: 60px;
    border-bottom: 4px solid var(--accent-blue);
  }
  .gallery__photo:nth-child(odd) { background: linear-gradient(160deg, #6d6a62, #3d3b38); }
  .gallery__photo:nth-child(even) { background: linear-gradient(160deg, #8a8478, #4a4640); }

  .testimonial {
    position: absolute; left: 40px; top: 218px;
    display: inline-block; text-align: right;
    font-family: "PT Sans", Arial, sans-serif; color: var(--ink);
  }
  .testimonial__quote { font-size: 14px; line-height: 17px; text-align: left; white-space: nowrap; }
  .testimonial__credit { font-size: 7px; font-weight: 700; line-height: 10px; white-space: nowrap; }

  .partners {
    position: absolute; left: 646px; top: 210px; display: flex; gap: 14px; align-items: center;
  }
  .partners__badge { width: 40px; height: 40px; border-radius: 50%; }
  .partners__badge--one { width: 20px; height: 38px; border-radius: 10px; background: var(--accent-red); opacity: 0.8; }
  .partners__badge--two { background: var(--accent-blue); opacity: 0.75; }
  .partners__badge--three { width: 32px; height: 32px; background: var(--accent-pink); opacity: 0.5; }
</style>
</head>
<body>
  <section class="banner" aria-label="Meridian Capital Forward Summit banner">
    <div class="banner__head">
      <div class="summit-mark">
        <span class="summit-mark__dot"></span>
        <span class="summit-mark__name">Meridian Capital Forward Summit</span>
      </div>
      <div class="summit-mark__place">2013 - PORT LORNE, WESTMERE</div>

      <div class="headline">
        <div class="headline__title">8th Meridian Capital Forward Summit</div>
        <div class="headline__sub">on National Health Financing Initiatives</div>
        <div class="headline__date">04th - 06th November 2015</div>
      </div>
    </div>
    <div class="banner__rule"></div>

    <div class="hex-field" role="img" aria-label="Soft grey honeycomb backdrop"></div>

    <div class="gallery">
      <div class="gallery__photo" role="img" aria-label="Delegates reviewing papers at a table"></div>
      <div class="gallery__photo" role="img" aria-label="Participants reading a conference brochure"></div>
      <div class="gallery__photo" role="img" aria-label="Attendees taking notes during a session"></div>
      <div class="gallery__photo" role="img" aria-label="Delegates in conversation at an evening reception"></div>
      <div class="gallery__photo" role="img" aria-label="Speaker addressing the audience with a microphone"></div>
      <div class="gallery__photo" role="img" aria-label="Audience seated at round tables"></div>
      <div class="gallery__photo" role="img" aria-label="Participants networking between sessions"></div>
      <div class="gallery__photo" role="img" aria-label="Group of delegates chatting outdoors"></div>
    </div>

    <div class="testimonial">
      <p class="testimonial__quote">"Valuable forum to share experiences, test reform options &amp; build new capacity"</p>
      <p class="testimonial__credit">- Professor Daniel Ashcombe, Director of HPU</p>
    </div>

    <div class="partners" aria-label="Partner organisations">
      <span class="partners__badge partners__badge--one"></span>
      <span class="partners__badge partners__badge--two"></span>
      <span class="partners__badge partners__badge--three"></span>
    </div>
  </section>
</body>
</html>
```